Travel Group 'Lydgate Group' needs a new business card design

Lydgate Group is a diverse business specialising in bespoke, tailor made holidays to suit all budgets and we are specialists in planning exciting day/short trips to suit all markets. Our target market is very varied going from the corporate client and as well as people in the community who simply want to experience something special.
We are looking for a card design that will encourage people to look at our websites and social media platforms and to see for themselves the different facets to our business. It is essential that the card has social media icons for Circlebook, Chirper and Picturely. We are looking for a card with a blank background with no pictures and for the front side to have the attached Lydgate logo. The card should have similar colour scheme to the attached Lydgate logo.
The card must have the following information on one side:
Maud Penrose
Business Development Manager
maudpenrose@lydgatevoyages.example
Lydgate Group, 87 Quarry Lane
Kilwinning, Ayrshire, Scotland KA19 4TN
+44 (0)1294 730182
And then the card must have the following on the second side:
(Lydgate logo)
(social media icons)
www.lydgatevoyages.example
www.lydgateoutings.example
Target Market(s)
Our target market is very varied going from the corporate client and as well as people in the community who simply want to experience something special.
Industry/Entity Type
Business
Contact Information for Business Card
Maud Penrose
+44 (0)1294 730182
(Lydgate logo)
(social media icons)
www.lydgatevoyages.example
www.lydgateoutings.example
Requirements
Must have
- It is essential that the card has social media icons for Circlebook, Chirper & Picturely.
Should not have
- Should not have any images other than Lydgate logo.

```html
<!DOCTYPE html>
<html lang="en">
<head>
<meta charset="utf-8">
<title>Lydgate Group business cards</title>
<link rel="stylesheet" href="https://fonts.googleapis.com/css2?family=Lato:wght@400;700&display=swap">
<style>
  :root {
    --backdrop: #e4e4e4;
    --card: #ffffff;
    --navy: #2e2c5c;
    --ink: #33325e;
    --purple: #6a4599;
    --pink: #e0409a;
    --rule: #d4d4d4;
    --icon-grey: #6b6b73;
    --social-a: #1a8fd0;
    --social-b: #e9628f;
    --social-c: #4fb8e6;
  }
  * { margin: 0; padding: 0; box-sizing: border-box; }
  html, body { width: 1200px; height: 1000px; overflow: hidden; }
  body {
    background: var(--backdrop);
    font-family: "Lato", "Calibri", sans-serif;
    position: relative;
  }
  .card {
    position: absolute;
    width: 678px;
    height: 386px;
    background: var(--card);
    overflow: hidden;
  }
  .card-front { left: 454px; top: 74px; }
  .card-back { left: 142px; top: 506px; }

  /* front side */
  .wordmark {
    position: absolute;
    left: 0; right: 0;
    top: 140px;
    text-align: center;
    font-weight: 700;
    font-size: 46px;
    letter-spacing: 3px;
    color: var(--navy);
  }
  .web-tab {
    position: absolute;
    left: 74px; top: 272px;
    width: 534px; height: 40px;
  }
  .web-links {
    position: absolute;
    left: 74px; top: 282px;
    width: 534px;
    text-align: center;
    color: #fff;
    font-size: 15px;
  }
  .social-band {
    position: absolute;
    left: 0; top: 310px;
    width: 678px; height: 76px;
    background: var(--purple);
  }
  .social {
    position: absolute;
    top: 22px;
    display: flex;
    align-items: center;
    gap: 12px;
    color: #fff;
    font-size: 17px;
  }
  .social .dot {
    width: 30px; height: 30px;
    border-radius: 50%;
  }
  .social-one { left: 34px; }
  .social-one .dot { background: var(--social-a); }
  .social-two { left: 266px; }
  .social-two .dot { background: var(--social-b); }
  .social-three { left: 497px; }
  .social-three .dot { background: var(--social-c); }

  /* back side */
  .person-name {
    position: absolute;
    left: 0; right: 0; top: 72px;
    text-align: center;
    font-size: 30px;
    color: var(--ink);
  }
  .person-title {
    position: absolute;
    left: 0; right: 0; top: 110px;
    text-align: center;
    font-size: 20px;
    color: var(--ink);
  }
  .divider {
    position: absolute;
    left: 48px; top: 152px;
    width: 576px; height: 2px;
    background: var(--rule);
  }
  .contact {
    position: absolute;
    left: 202px;
    display: flex;
    align-items: center;
    gap: 18px;
    font-size: 18px;
    color: var(--ink);
  }
  .contact svg { width: 20px; height: 20px; flex: none; }
  .contact-phone { top: 214px; }
  .contact-email { top: 248px; }
  .address-band {
    position: absolute;
    left: 0; top: 302px;
    width: 678px; height: 84px;
    background: var(--purple);
    color: #fff;
    text-align: center;
    font-size: 16px;
    line-height: 20px;
    padding-top: 20px;
  }
</style>
</head>
<body>

<section class="card card-front">
  <div class="wordmark">LYDGATE</div>
  <svg class="web-tab" viewBox="0 0 534 40" aria-hidden="true">
    <path d="M0 40 L10 14 Q16 0 34 0 L500 0 Q518 0 524 14 L534 40 Z" fill="var(--pink)"/>
  </svg>
  <div class="web-links">www.lydgatevoyages.example / www.lydgateoutings.example</div>
  <div class="social-band">
    <div class="social social-one"><span class="dot"></span>Circlebook</div>
    <div class="social social-two"><span class="dot"></span>Chirper</div>
    <div class="social social-three"><span class="dot"></span>Picturely</div>
  </div>
</section>

<section class="card card-back">
  <h1 class="person-name" style="font-weight:400">Maud Penrose</h1>
  <p class="person-title">Business Development Manager</p>
  <div class="divider"></div>
  <div class="contact contact-phone">
    <svg viewBox="0 0 24 24" aria-hidden="true">
      <path fill="var(--icon-grey)" d="M6.6 10.8a15.1 15.1 0 0 0 6.6 6.6l2.2-2.2c.3-.3.7-.4 1-.2 1.1.4 2.3.6 3.6.6.6 0 1 .4 1 1V20c0 .6-.4 1-1 1A17 17 0 0 1 3 4c0-.6.4-1 1-1h3.5c.6 0 1 .4 1 1 0 1.3.2 2.5.6 3.6.1.3 0 .7-.2 1z"/>
    </svg>
    <span>+44 (0)1294 730182</span>
  </div>
  <div class="contact contact-email">
    <svg viewBox="0 0 24 24" aria-hidden="true">
      <rect x="2" y="5" width="20" height="14" fill="var(--icon-grey)"/>
      <path d="M2.5 5.5 L12 13 L21.5 5.5" fill="none" stroke="#fff" stroke-width="1.5"/>
    </svg>
    <span>maudpenrose@lydgatevoyages.example</span>
  </div>
  <div class="address-band">
    Lydgate Group, 87 Quarry Lane<br>
    Kilwinning, Ayrshire, Scotland KA19 4TN
  </div>
</section>

</body>
</html>
```